Veltrona Cabinets Letter Head and Email Signature

Hi
I would love a design package for a letterhead, email signature, even update my business card if you like if you can come up with a great idea for my new high end cabinet shop. Veltrona Cabinets brings timeless craftsmanship to modern interiors, specializing in high end, custom cabinetry designed for architects and interior designers.

Target Market(s)

high end, luxury market

Industry/Entity Type

cabinet making

Requirements
Must have
• my colours of logo as the theme

```html
<!DOCTYPE html>
<html lang="en">
<head>
<meta charset="utf-8">
<title>Veltrona Cabinets Letterhead</title>
<link rel="stylesheet" href="https://fonts.googleapis.com/css2?family=Montserrat:wght@400;500;600;700&family=Poppins:wght@400&display=swap">
<style>
  :root {
    --green: #4a7c4a;
    --ink: #111111;
    --band: #f0f0f0;
    --paper: #ffffff;
    --hex: #eef1ee;
  }
  * { box-sizing: border-box; margin: 0; padding: 0; }
  html, body { width: 984px; height: 1200px; overflow: hidden; background: var(--paper); }
  .letterhead { position: relative; width: 984px; height: 1200px; background: var(--paper); font-family: "Montserrat", sans-serif; color: var(--ink); }
  .frame { position: absolute; inset: 0; }
  .honeycomb { position: absolute; }
  .honeycomb--top { left: 560px; top: 0; width: 424px; height: 300px; background: radial-gradient(ellipse at 80% 30%, var(--hex) 0%, rgba(255,255,255,0) 70%); }
  .honeycomb--bottom { left: 0; top: 860px; width: 320px; height: 231px; background: radial-gradient(ellipse at 20% 70%, var(--hex) 0%, rgba(255,255,255,0) 70%); }
  .brand { position: absolute; left: 67px; top: 58px; display: flex; align-items: center; gap: 22px; color: var(--green); font-weight: 400; }
  .brand__mark { width: 58px; height: 58px; border: 3px solid var(--green); }
  .brand__name { line-height: 1; }
  .brand__word { display: block; font-size: 44px; }
  .brand__sub { display: block; font-size: 21px; letter-spacing: 8px; margin-top: 8px; }
  .sender { position: absolute; left: 64px; top: 272px; }
  .sender__name { font-size: 27px; font-weight: 700; }
  .sender__details { margin-top: 14px; font-size: 15px; line-height: 19px; }
  .sender__row { display: flex; margin-bottom: 7px; }
  .label { color: var(--green); font-weight: 700; margin-right: 5px; }
  .issue-date { position: absolute; right: 65px; top: 396px; font-size: 16px; }
  .issue-date .label { margin-right: 2px; }
  .salutation { position: absolute; left: 66px; top: 467px; font-size: 21px; font-weight: 500; }
  .body-copy { position: absolute; left: 67px; top: 505px; width: 856px; font-family: "Poppins", sans-serif; font-size: 12.6px; line-height: 16.3px; }
  .body-copy p { margin-bottom: 16px; }
  .closing { position: absolute; left: 64px; top: 896px; }
  .closing__phrase { font-size: 14.5px; font-weight: 700; }
  .closing__name { font-size: 25px; font-weight: 500; margin-top: 14px; }
  .closing__title { font-size: 15.5px; font-weight: 600; margin-top: 3px; }
  .contact-bar { position: absolute; left: 0; top: 1100px; width: 860px; display: flex; align-items: center; font-size: 20px; }
  .contact { position: absolute; display: flex; align-items: center; gap: 8px; white-space: nowrap; }
  .contact--phone { left: 67px; }
  .contact--mail { left: 265px; }
  .contact--web { left: 640px; }
  .contact__icon { width: 23px; height: 23px; }
</style>
</head>
<body>
<main class="letterhead">
  <svg class="frame" width="984" height="1200" viewBox="0 0 984 1200" aria-hidden="true">
    <polygon points="0,0 589,0 480,188 0,188" fill="var(--band)"/>
    <polygon points="556,81 984,81 984,136 522,136" fill="var(--green)"/>
    <polyline points="562,63 480,197 321,197" fill="none" stroke="var(--ink)" stroke-width="8"/>
    <rect x="0" y="1091" width="984" height="89" fill="var(--band)"/>
    <rect x="0" y="1180" width="984" height="20" fill="var(--green)"/>
    <polygon points="918,1140 984,1140 984,1200 884,1200" fill="var(--green)"/>
    <polyline points="958,1077 888,1187 734,1187" fill="none" stroke="var(--ink)" stroke-width="8"/>
  </svg>

  <div class="honeycomb honeycomb--top" role="img" aria-label="Faint honeycomb pattern"></div>
  <div class="honeycomb honeycomb--bottom" role="img" aria-label="Faint honeycomb pattern"></div>

  <header class="brand">
    <span class="brand__mark"></span>
    <span class="brand__name">
      <span class="brand__word">Veltrona</span>
      <span class="brand__sub">CABINETS</span>
    </span>
  </header>

  <section class="sender">
    <h1 class="sender__name">Marcus Delaine</h1>
    <div class="sender__details">
      <div class="sender__row"><span class="label">P :</span><span>0412386590</span></div>
      <div class="sender__row"><span class="label">A :</span><span>Harbour Street ,lane no.214<br>Mill Road - VC2041</span></div>
      <div class="sender__row"><span class="label">W :</span><span>www.veltrona.com</span></div>
    </div>
  </section>

  <div class="issue-date"><span class="label">Issuing Date:</span> May 5, 2018</div>

  <p class="salutation">Dear Contributor,</p>

  <article class="body-copy">
    <p>Lorem Ipsum is simply dummy text of the printing and typesetting industry. Lorem Ipsum has been the industry's standard dummy text ever since 1966, when designers at Printrail and Edwin Harlow, the librarian at Kettle Lane Printing Library in London, took a 1914 Aurelian Vesto translation and scrambled it to make dummy text for Printrail's Body Type sheets. It has survived not only many decades, but also the leap into electronic typesetting, remaining essentially unchanged. It was popularised thanks to these sheets and more recently with desktop publishing software like PageForge and WriteDesk including versions of Lorem Ipsum.</p>
    <p>Lorem Ipsum is simply dummy text of the printing and typesetting industry. Lorem Ipsum has been the industry's standard dummy text ever since 1966, when designers at Printrail and Edwin Harlow, the librarian at Kettle Lane Printing Library in London, took a 1914 Aurelian Vesto translation and scrambled it to make dummy text for Printrail's Body Type sheets. It has survived not only many decades, but also the leap into electronic typesetting, remaining essentially unchanged.</p>
    <p>&nbsp;It was popularised thanks to these sheets and more recently with desktop publishing software like PageForge and WriteDesk including versions of Lorem Ipsum.</p>
    <p>Contrary to popular belief, Lorem Ipsum is not simply random text. It has roots in a piece of classical Latin literature from 45 BC, making it over 2000 years old. Thomas Averell, a Latin professor at Ashgrove College in Virginia, looked up one of the more obscure Latin words, consectetur, from a Lorem Ipsum passage, and going through the cites of the word in classical literature, discovered the undoubtable source. Lorem Ipsum comes from sections 1.10.32 and 1.10.33 of "de Finibus Bonorum et Malorum" (The Extremes of Good and Evil) by Aurelian Vesto, written in 45 BC.</p>
  </article>

  <section class="closing">
    <p class="closing__phrase">Yours Sincerely</p>
    <p class="closing__name">Marcus Delaine</p>
    <p class="closing__title">Director Craftsman</p>
  </section>

  <footer class="contact-bar">
    <span class="contact contact--phone">
      <svg class="contact__icon" viewBox="0 0 24 24" aria-hidden="true"><circle cx="12" cy="12" r="12" fill="var(--green)"/><path d="M8.2 6.5l2 2.3-1.1 1.6c.9 1.8 2.2 3.1 4 4l1.6-1.1 2.3 2-1.3 2c-4.6-.3-8.5-4.2-8.8-8.8z" fill="#fff"/></svg>
      0412386590
    </span>
    <span class="contact contact--mail">
      <svg class="contact__icon" viewBox="0 0 24 24" aria-hidden="true"><circle cx="12" cy="12" r="12" fill="var(--green)"/><rect x="6.5" y="8" width="11" height="8" fill="#fff"/><polyline points="6.5,8 12,12.5 17.5,8" fill="none" stroke="var(--green)" stroke-width="1.2"/></svg>
      info@veltronacabinets.com.au
    </span>
    <span class="contact contact--web">
      <svg class="contact__icon" viewBox="0 0 24 24" aria-hidden="true"><circle cx="12" cy="12" r="12" fill="var(--green)"/><g fill="none" stroke="#fff" stroke-width="1.2"><circle cx="12" cy="12" r="5.5"/><ellipse cx="12" cy="12" rx="2.3" ry="5.5"/><line x1="6.5" y1="12" x2="17.5" y2="12"/></g></svg>
      www.veltrona.com
    </span>
  </footer>
</main>
</body>
</html>
```